依頼詳細
背景は白で、シンプルだけど、ひとひねりの意味のあるスタイリッシュで知的なデザインを希望しております。カラフルでは無く、モダンで未来的なニュアンスがあると尚良いです。

裏面は、事業内容を3つ掲載したいです。
裏面は、とにかくシンプルが良いです。

書体は明朝とゴシックのどちらの案も見てみたいです。

※会社ロゴを添付いたしますので、色調をなるべく合わせていただきたいです。
※サイトから会社の雰囲気を読み取っていただきたいです。
URL:http://brightlanexy.com/

紙は、厚みのある固めの高級紙を使用します。
記載項目
(表面)・会社ロゴ ・名前:佐藤春樹  ・ふりがな:(Sato Haruki)
・役職:マーケティングディレクター ・ふりがな:(Marketing Director)
・電話番号:029-481-7263
・メール全体:info@brightlanexy.com
・メール個人:h.sato@brightlanexy.com
・URL:http://brightlanexy.com/
・住所:〒310-0844 茨城県水戸市住吉町4-208-2
(裏面)・事業内容のみ▶︎ ウェブ制作 ウェブ広告運用 ECコンサルタント
希望イメージ
シンプル 複雑
単色 カラフル
暗い 明るい
日常 高級
遊び心 厳粛
未来的 伝統的
女性的 男性的
希望する色
青系

全体的に、シンプルだけど品があってかっこいいです。

ただのシンプルとは違い、遊び心が上手く出ているのがとても良いです。

ちょっとした一つの文字の配置の仕方で大きく変わるものなのだなと感心いたしました。

皆さんこのたびはご協力いただきまして誠にありがとうございました。

```html
<!DOCTYPE html>
<html lang="ja">
<head>
<meta charset="UTF-8">
<title>Brightlane XY LLC. 名刺</title>
<link rel="stylesheet" href="https://fonts.googleapis.com/css2?family=Noto+Sans+JP:wght@400;500;700&family=Open+Sans:wght@400;700&display=swap">
<style>
  :root {
    --page: #ffffff;
    --card: #ffffff;
    --card-edge: #c9c9c9;
    --ink: #333333;
    --ink-soft: #555555;
    --brand: #2f4f6f;
    --brand-dot: #3d8fd1;
    --band: rgba(95, 169, 216, 0.22);
  }
  * { margin: 0; padding: 0; box-sizing: border-box; }
  html, body {
    width: 829px; height: 1200px; overflow: hidden;
    background: var(--page);
    font-family: "Noto Sans JP", "Open Sans", sans-serif;
    color: var(--ink);
  }
  .sheet { position: relative; width: 829px; height: 1200px; }
  .card {
    position: absolute; left: 50px; width: 729px; height: 512px;
    background: var(--card); border: 1.5px solid var(--card-edge);
    overflow: hidden;
  }
  .card--front { top: 50px; }
  .card--back { top: 610px; }
  .accent-band {
    position: absolute; left: -40px; right: -40px; height: 70px;
    background: linear-gradient(to bottom, transparent, var(--band), transparent);
    transform: rotate(-7deg);
  }
  .card--front .accent-band { top: 140px; }
  .card--back .accent-band { top: 180px; }
  .brand {
    position: absolute; display: flex; align-items: center; gap: 8px;
    font-family: "Open Sans", sans-serif; font-weight: 700;
    color: var(--brand); line-height: 1.2;
  }
  .brand__name { display: block; }
  .brand__dot { width: 22px; height: 22px; border-radius: 50%; background: var(--brand-dot); flex: none; }
  .card--front .brand { left: 22px; top: 22px; font-size: 27px; }
  .card--front .brand .brand__dot { width: 30px; height: 30px; }
  .identity { position: absolute; right: 22px; top: 232px; text-align: right; }
  .identity__role { font-size: 17px; color: var(--ink-soft); letter-spacing: 0.04em; }
  .identity__name { margin-top: 10px; font-size: 40px; font-weight: 400; letter-spacing: 0.08em; color: var(--ink); }
  .identity__name-en { font-size: 17px; letter-spacing: 0.02em; margin-left: 18px; color: var(--ink-soft); }
  .identity__mail { margin-top: 8px; font-size: 17px; color: var(--ink-soft); letter-spacing: 0.03em; }
  .contact { position: absolute; left: 22px; top: 390px; font-size: 17px; line-height: 1.62; color: var(--ink-soft); letter-spacing: 0.03em; }
  .contact__address span { margin-left: 22px; }
  .services { position: absolute; left: 0; right: 0; text-align: center; }
  .services__heading { top: 150px; font-size: 17px; letter-spacing: 0.08em; }
  .services__list { top: 285px; font-size: 20px; letter-spacing: 0.06em; color: var(--ink-soft); }
  .card--back .brand { left: 50%; transform: translateX(-50%); top: 410px; font-size: 17px; text-align: center; }
</style>
</head>
<body>
<main class="sheet">
  <section class="card card--front" aria-label="名刺 表面">
    <div class="accent-band" role="img" aria-label="流れるような青い曲線の装飾"></div>
    <div class="brand">
      <div><span class="brand__name">Brightlane XY</span><span class="brand__name">LLC.</span></div>
      <span class="brand__dot"></span>
    </div>
    <div class="identity">
      <p class="identity__role">マーケティングディレクター&nbsp; Marketing Director</p>
      <p class="identity__name">佐藤 春樹<span class="identity__name-en">Sato Haruki</span></p>
      <p class="identity__mail">E-mail:h.sato@brightlanexy.com</p>
    </div>
    <div class="contact">
      <p class="contact__address">〒310-0844<span>茨城県水戸市住吉町4-208-2</span></p>
      <p>Tel:029-481-7263</p>
      <p>E-mail:info@brightlanexy.com</p>
      <p>URL:http://brightlanexy.com/</p>
    </div>
  </section>

  <section class="card card--back" aria-label="名刺 裏面">
    <div class="accent-band" role="img" aria-label="流れるような青い曲線の装飾"></div>
    <p class="services services__heading">事業内容</p>
    <p class="services services__list">ウェブ制作 / ウェブ広告運用 /EC コンサルタント</p>
    <div class="brand">
      <div><span class="brand__name">Brightlane XY</span><span class="brand__name">LLC.</span></div>
      <span class="brand__dot"></span>
    </div>
  </section>
</main>
</body>
</html>
```